Modern Catering Company needs Letterhead Design

We need a letterhead design that will make effective use of the corporate logo and color scheme, along with careful typography, helps this letterhead design communicate the brand well. We do have a corporate logo, however feel free to enhance the color scheme with gold and purple. We are serving a very upscale clientele so the letterhead has to reflect elegance, professionalism, cleanliness, and modern style. We are branding the company so the letterhead and business cards must fit the brand story. There should be no cartoonish elements in the design and we are looking for sharper lines.

Target Market(s)

Businesses and upscale clientele

Industry/Entity Type

Catering

Contact Information for Business Card

while this design can have any number of quirks and distinctions, it needs to be cohesive with the entire brand story clean, professional but edgy

Requirements
Must have
• must have good and carefully placement of it’s logo and where you place the text or the message. Colors blue, very deep purple, jewel tones not pastels, gold. Blue must be the primary color you may accent with purple or gold. Contact information is as follows: Co-Owners/ Chefs: R. Hollowmere & L. Brandt, phone: 414-555-0182 email:Contact@orchardtablecatering.example, address: 6127 W Larkspur Hollow Rd, Milwaukee, WI 53299
Should not have
• pastel colors, Do not add the BBQ information to the letterhead or business card it was a mistake by the previous designer.

```html
<!DOCTYPE html>
<html lang="en">
<head>
<meta charset="utf-8">
<title>Orchard Table Catering – Business Card</title>
<link rel="stylesheet" href="https://fonts.googleapis.com/css2?family=Arimo:wght@400;700&display=swap">
<style>
  :root {
    --page-bg: #d9d5cf;
    --card-bg: #eef0f1;
    --purple: #2c2466;
    --gold-dark: #b5822a;
    --gold: #e6b13d;
    --gold-light: #f2c75a;
    --ink: #2a2340;
  }
  * { margin: 0; padding: 0; box-sizing: border-box; }
  html, body { width: 1200px; height: 969px; overflow: hidden; }
  body {
    background: var(--page-bg);
    font-family: "Arimo", Arial, sans-serif;
    color: var(--ink);
    position: relative;
  }
  .business-card {
    position: absolute;
    left: 100px;
    top: 201px;
    width: 1000px;
    height: 567px;
    background: var(--card-bg);
    overflow: hidden;
    box-shadow: 0 6px 24px rgba(0,0,0,0.18);
  }
  .card-wave {
    position: absolute;
    inset: 0;
    width: 100%;
    height: 100%;
  }
  .brand {
    position: absolute;
    right: 44px;
    top: 36px;
    width: 440px;
    text-align: center;
    color: var(--purple);
    font-weight: 400;
  }
  .brand-mark {
    width: 60px;
    height: 60px;
    border-radius: 50%;
    background: var(--purple);
    margin: 0 auto 20px;
  }
  .brand-name {
    font-size: 48px;
    line-height: 1.05;
    letter-spacing: 0.01em;
    text-transform: uppercase;
  }
  .brand-name span {
    display: block;
    font-size: 34px;
    letter-spacing: 0.34em;
    margin-top: 8px;
    padding-left: 0.34em;
  }
  .address {
    position: absolute;
    left: 67px;
    top: 313px;
    font-size: 25px;
    line-height: 34px;
  }
  .contact-list {
    position: absolute;
    left: 67px;
    top: 414px;
    list-style: none;
    font-size: 25px;
  }
  .contact-list li {
    display: flex;
    align-items: center;
    height: 38px;
  }
  .contact-list svg {
    width: 22px;
    height: 22px;
    margin-right: 16px;
    fill: var(--purple);
    flex: none;
  }
  .person {
    position: absolute;
    right: 64px;
    top: 446px;
    text-align: right;
  }
  .person-name {
    font-size: 31px;
    font-weight: 700;
    color: var(--purple);
    line-height: 38px;
  }
  .person-title {
    font-size: 25px;
    color: var(--purple);
    line-height: 36px;
  }
</style>
</head>
<body>
  <div class="business-card">
    <svg class="card-wave" viewBox="0 0 550 312" preserveAspectRatio="none" aria-hidden="true">
      <defs>
        <linearGradient id="goldFill" x1="0" y1="0" x2="1" y2="0.3">
          <stop offset="0" stop-color="var(--gold-dark)"/>
          <stop offset="0.45" stop-color="var(--gold-light)"/>
          <stop offset="0.75" stop-color="var(--gold)"/>
          <stop offset="1" stop-color="var(--gold-dark)"/>
        </linearGradient>
      </defs>
      <path d="M0,146 C120,112 250,163 350,203 C430,234 520,214 550,150 L550,312 L0,312 Z" fill="url(#goldFill)"/>
      <path d="M0,141 C120,106 250,155 350,195 C430,226 520,206 550,145 L550,150 C520,214 430,234 350,203 C250,163 120,112 0,146 Z" fill="var(--purple)"/>
    </svg>

    <div class="brand">
      <div class="brand-mark"></div>
      <div class="brand-name">Orchard Table<span>Catering</span></div>
    </div>

    <p class="address">6127 W Larkspur Hollow Rd<br>Milwaukee, WI 53299</p>

    <ul class="contact-list">
      <li>
        <svg viewBox="0 0 24 24" aria-hidden="true"><path d="M6.6 10.8a15.1 15.1 0 0 0 6.6 6.6l2.2-2.2c.3-.3.7-.4 1-.2 1.1.4 2.3.6 3.6.6.6 0 1 .4 1 1V20c0 .6-.4 1-1 1A17 17 0 0 1 3 4c0-.6.4-1 1-1h3.5c.6 0 1 .4 1 1 0 1.3.2 2.5.6 3.6.1.3 0 .7-.2 1z"/></svg>
        414-555-0182
      </li>
      <li>
        <svg viewBox="0 0 24 24" aria-hidden="true"><path d="M2 5h20v14H2z M3.5 6.5 12 13l8.5-6.5" fill="var(--purple)" stroke="var(--card-bg)" stroke-width="1.4"/></svg>
        Contact@orchardtablecatering.example
      </li>
      <li>
        <svg viewBox="0 0 24 24" aria-hidden="true"><circle cx="12" cy="12" r="10"/><path d="M2 12h20M12 2c3 3 3 17 0 20M12 2c-3 3-3 17 0 20" fill="none" stroke="var(--card-bg)" stroke-width="1.4"/></svg>
        www.orchardtablecatering.example
      </li>
    </ul>

    <div class="person">
      <p class="person-name">R. Hollowmere</p>
      <p class="person-title">Co-Owner / Chef</p>
    </div>
  </div>
</body>
</html>
```